Stock Market Research Company Needs a new Design for our Podcast

We need a new logo and social media images for our podcast called Ledger Chat Podcast. We have a current design and logo but are looking to update the branding of the podcast. The podcast is highly interactive taking listener questions each week on individual stocks as well as stock portfolio building strategies.

Copy of Ledger Chat Podcast Thumbnail is our current branding.

Podcast Ad 2 Image attached for an idea of what we're looking for but using our specific colours.

Incorporate K from our current logo (attached)
Colours: Primary Color: (#1AA897), Secondary Color (#2E4151)
Clean/Modern style
Include Headshots of Hosts (images attached)

Target Market(s)

Podcast listeners and stock market investors

Industry/Entity Type

Investment

Logo Text

Title - Ledger Chat Podcast. Tagline - Stock Picks, Strategies & Tips For All Investors

Colors
33b8a4
86cfc6
00a990

Requirements
Must have
• Incorporate K from our current logo (attached)
Clean/Modern style

```html
<!DOCTYPE html>
<html lang="en">
<head>
<meta charset="utf-8">
<title>Ledger Chat Podcast</title>
<link rel="stylesheet" href="https://fonts.googleapis.com/css2?family=Bebas+Neue&family=Anton&family=Montserrat:wght@400&display=swap">
<style>
  :root {
    --bg: #000000;
    --gold: #dcc52a;
    --teal-soft: #6aa69b;
    --teal-band: #659e94;
    --podcast-gold: #cbab2e;
    --white: #ffffff;
    --ink: #0b0b0b;
  }
  html, body {
    margin: 0;
    padding: 0;
    width: 1200px;
    height: 1200px;
    overflow: hidden;
    background: var(--bg);
  }
  .cover {
    position: relative;
    width: 1200px;
    height: 1200px;
    background: var(--bg);
    font-family: "Bebas Neue", "Oswald", sans-serif;
  }
  .tagline {
    position: absolute;
    left: 0;
    width: 1200px;
    text-align: center;
    margin: 0;
    font-weight: 400;
    font-size: 84px;
    line-height: 1;
    letter-spacing: 9px;
  }
  .tagline--top { top: 52px; color: var(--gold); }
  .tagline--bottom { top: 138px; color: var(--teal-soft); letter-spacing: 8px; }
  .hosts {
    position: absolute;
    left: 137px;
    top: 237px;
    width: 933px;
    height: 426px;
    border-radius: 160px 160px 0 0;
    background: linear-gradient(180deg, #2a2a2e 0%, #3c3f47 45%, #e8e6e2 100%);
  }
  .title-band {
    position: absolute;
    left: 93px;
    top: 663px;
    width: 1013px;
    height: 287px;
    background: var(--teal-band);
  }
  .title-band svg { display: block; }
  .title-text {
    font-family: "Anton", "Oswald", sans-serif;
    fill: var(--white);
  }
  .podcast-label {
    position: absolute;
    left: 374px;
    top: 916px;
    width: 466px;
    height: 73px;
    background: var(--podcast-gold);
    color: var(--ink);
    display: flex;
    align-items: center;
    justify-content: center;
    font-size: 66px;
    letter-spacing: 22px;
    padding-left: 22px;
    box-sizing: border-box;
  }
  .brand {
    position: absolute;
    left: 287px;
    top: 1064px;
    display: flex;
    align-items: center;
    gap: 22px;
  }
  .brand-mark {
    width: 82px;
    height: 82px;
    background: var(--teal-soft);
  }
  .brand-name {
    display: flex;
    flex-direction: column;
    gap: 14px;
  }
  .brand-name .firm,
  .brand-name .descriptor {
    font-family: "Montserrat", sans-serif;
    font-weight: 400;
    color: var(--white);
    line-height: 1;
    white-space: nowrap;
  }
  .brand-name .firm {
    font-size: 40px;
    letter-spacing: 3px;
  }
  .brand-name .descriptor {
    font-size: 22px;
    letter-spacing: 4px;
  }
</style>
</head>
<body>
  <main class="cover">
    <p class="tagline tagline--top">Stock Picks, Strategies</p>
    <p class="tagline tagline--bottom">&amp; Tips For Investors</p>

    <div class="hosts" role="img" aria-label="Headshots of the two podcast hosts in dark suits and white shirts, side by side"></div>

    <div class="title-band">
      <svg width="1013" height="287" viewBox="0 0 1013 287" aria-label="Ledger Chat">
        <text class="title-text" x="506" y="222" text-anchor="middle" font-size="200" textLength="940" lengthAdjust="spacingAndGlyphs">LEDGER CHAT</text>
      </svg>
    </div>

    <div class="podcast-label">PODCAST</div>

    <div class="brand">
      <div class="brand-mark"></div>
      <div class="brand-name">
        <span class="firm">RIDGEWAY PARTNERS</span>
        <span class="descriptor">INDEPENDENT MARKET RESEARCH</span>
      </div>
    </div>
  </main>
</body>
</html>
```